Awesome Flyer for Tactical Emergency Response Services

We need a Flyer for Emergency Rapid Response services for my company ferncrest Security Services Ltd. , we are a security guisard service based in Trinidad in the Caribbean.
The flyer will include price and pictures of our tactical team. must be clear concise, and strong.

Rapid response services is where customers pay a monthly fee and if they have any security issues they call us and we immediately respond to their home or business to ensure their safety and security.

Target Market(s)

Homeowners; people worried about home security such as home invasions etc.

Requirements
Must have
• Company Logo prominent

```html
<!DOCTYPE html>
<html lang="en">
<head>
<meta charset="utf-8">
<title>Ferncrest Security Services – Rapid Response Flyer</title>
<link rel="stylesheet" href="https://fonts.googleapis.com/css2?family=Montserrat:wght@400;500;700;800&family=Oswald:wght@600&display=swap">
<style>
  :root{
    --page:#c9c9c9;
    --black:#0d0d0f;
    --charcoal:#2a2b2d;
    --steel:#4a4c50;
    --silver:#d9dbde;
    --red:#d3222c;
    --red-deep:#a8161e;
    --white:#ffffff;
  }
  *{margin:0;padding:0;box-sizing:border-box}
  html,body{width:1200px;height:960px;overflow:hidden;background:var(--page)}
  body{font-family:"Montserrat",Arial,sans-serif;color:var(--white)}
  .flyer{position:absolute;left:282px;top:30px;width:636px;height:900px;overflow:hidden;background:var(--charcoal);box-shadow:0 6px 24px rgba(0,0,0,.25)}
  .flyer-art{position:absolute;inset:0}
  .photo{position:absolute;inset:0;width:636px;height:900px}
  .brand{position:absolute;left:0;right:0;top:54px;display:flex;align-items:center;justify-content:center;gap:14px}
  .brand-mark{width:34px;height:34px;background:var(--red)}
  .brand-name{font-weight:700;font-size:24px;letter-spacing:2px;text-transform:uppercase;color:var(--white)}
  .offer{position:absolute;left:34px;top:505px;width:340px}
  .headline{font-weight:800;font-size:30px;line-height:1.05;letter-spacing:.3px;white-space:nowrap}
  .headline .accent{display:block;color:var(--red);font-size:32px}
  .benefits{list-style:none;margin-top:12px;width:330px}
  .benefits li{position:relative;padding-left:18px;font-size:14px;font-weight:500;line-height:1.3;margin-bottom:6px}
  .benefits li::before{content:"★";position:absolute;left:0;top:1px;color:var(--red);font-size:11px}
  .price-box{position:absolute;left:38px;top:708px;width:290px;padding:12px 16px;background:var(--black);outline:3px dashed var(--red);outline-offset:4px}
  .price{font-family:"Oswald",Impact,sans-serif;font-weight:600;font-size:25px;line-height:1.2;letter-spacing:.3px;white-space:nowrap}
  .price-note{font-size:15px;font-weight:700;line-height:1.25;margin-top:2px}
  .price-note .hl{color:var(--red)}
  .contact-bar{position:absolute;left:0;right:0;bottom:0;height:66px;background:linear-gradient(var(--red),var(--red-deep));display:flex;align-items:center;justify-content:space-around;padding:0 18px}
  .contact{display:flex;align-items:center;gap:8px;font-size:14px;font-weight:500}
  .contact svg{width:16px;height:16px}
</style>
</head>
<body>
<main class="flyer">
  <svg class="flyer-art" viewBox="0 0 636 900" aria-hidden="true">
    <defs>
      <linearGradient id="plate" x1="0" y1="0" x2="0" y2="1">
        <stop offset="0" stop-color="#1c1c1e"/><stop offset="1" stop-color="#050506"/>
      </linearGradient>
      <linearGradient id="hex" x1="0" y1="0" x2="1" y2="1">
        <stop offset="0" stop-color="#2e2f31"/><stop offset="1" stop-color="#48494c"/>
      </linearGradient>
    </defs>
    <rect width="636" height="900" fill="url(#hex)"/>
    <rect width="636" height="240" fill="url(#plate)"/>
  </svg>

  <svg class="photo" viewBox="0 0 636 900" role="img" aria-label="Photo of the armed tactical response team in vests standing in front of branded red and white patrol cars">
    <defs>
      <linearGradient id="team" x1="0" y1="0" x2="0" y2="1">
        <stop offset="0" stop-color="#8f918f"/><stop offset=".55" stop-color="#6c6e6b"/><stop offset="1" stop-color="#5d7a3a"/>
      </linearGradient>
    </defs>
    <path d="M0,150 Q318,250 636,150 L636,455 Q318,395 0,505 Z" fill="url(#team)" stroke="#d9dbde" stroke-width="5"/>
  </svg>

  <svg class="photo" viewBox="0 0 636 900" role="img" aria-label="Photo of tactical officers crouched in formation aiming rifles beside a wall">
    <defs>
      <linearGradient id="drill" x1="0" y1="0" x2="0" y2="1">
        <stop offset="0" stop-color="#4a4c4e" stop-opacity="0"/><stop offset=".35" stop-color="#6f706e"/><stop offset="1" stop-color="#55733a"/>
      </linearGradient>
    </defs>
    <path d="M350,480 L636,440 L636,834 L350,834 Z" fill="url(#drill)"/>
  </svg>

  <div class="brand">
    <span class="brand-mark"></span>
    <span class="brand-name">Ferncrest Security Services</span>
  </div>

  <section class="offer">
    <h1 class="headline">24 HR EMERGENCY<span class="accent">RAPID RESPONSE</span></h1>
    <ul class="benefits">
      <li>Fully equipped and specially trained in tactical rapid response protocols</li>
      <li>Protecting you 24/7</li>
      <li>Delivering Peace of mind<br>to our clients</li>
    </ul>
  </section>

  <div class="price-box">
    <p class="price">$200 + VAT PER MONTH</p>
    <p class="price-note">Sign up for <span class="hl">12 months</span> &amp;<br>receive a <span class="hl">10% discount</span></p>
  </div>

  <footer class="contact-bar">
    <span class="contact">
      <svg viewBox="0 0 24 24"><path fill="#fff" d="M6.6 10.8a15 15 0 0 0 6.6 6.6l2.2-2.2a1 1 0 0 1 1-.25 11.4 11.4 0 0 0 3.6.6 1 1 0 0 1 1 1V20a1 1 0 0 1-1 1A17 17 0 0 1 3 4a1 1 0 0 1 1-1h3.5a1 1 0 0 1 1 1c0 1.25.2 2.45.6 3.6a1 1 0 0 1-.25 1z"/></svg>
      555-0184 / 555-0192
    </span>
    <span class="contact">
      <svg viewBox="0 0 24 24"><rect x="2" y="5" width="20" height="14" rx="2" fill="#fff"/><path d="M3 6l9 7 9-7" fill="none" stroke="#a8161e" stroke-width="2"/></svg>
      info@ferncrest-tt.com
    </span>
    <span class="contact">
      <svg viewBox="0 0 24 24" fill="none" stroke="#fff" stroke-width="2"><circle cx="12" cy="12" r="9"/><path d="M3 12h18M12 3c3 3 3 15 0 18M12 3c-3 3-3 15 0 18"/></svg>
      www.ferncrest-tt.com
    </span>
  </footer>
</main>
</body>
</html>
```